I need a business card for my original fine art pieces

I would like a business card design including a logo design for a new business in the art world. I am based in the Hunter Valley NSW Australia. I am a contemporary figurative, encaustic and wildlife artist. I would like to be able to upload my email and mobile number to this as well. This design should be one that I can incorporate into banners and flyers etc. Id like to incorporate one of my own images or partial image into the background or somewhere below. My initials are KR and I would like these used as a logo type. I would like the use of some colour and it to be bright and catchy. The final design should communicate artwork custom made and commissions available.

Overview: Original Fine Artworks for sale, online, art galleries etc, Custom made to order and by commission.

Target market is world wide audience and corporate world

My figurative work is painted using acrylics in a lot of natural ochre colours that reflect the Australian Outback, on canvas, linen, paper or board: My encaustic work is created in a contemporary abstract style using a blow torch and a made with a medium of 100% pure bees wax, Damar resin, mixed media and coloured pigments, applied to Birch board. My wildlife are created using coloured pencil and mixed media on a variety of paper types or board.

```html
<!DOCTYPE html>
<html lang="en">
<head>
<meta charset="utf-8">
<title>Kara Reid – Business Card</title>
<link rel="stylesheet" href="https://fonts.googleapis.com/css2?family=Source+Sans+3:wght@400;600&display=swap">
<style>
  :root {
    --bg-top: #2b2b2b;
    --bg-bottom: #050505;
    --card-front: #ffffff;
    --card-back: #f3f3f3;
    --accent: #ef4812;
    --ink: #4a4a4a;
    --ink-dark: #111111;
  }
  html, body {
    margin: 0;
    padding: 0;
    width: 1200px;
    height: 900px;
    overflow: hidden;
  }
  .stage {
    position: relative;
    width: 1200px;
    height: 900px;
    background: linear-gradient(180deg, var(--bg-top) 0%, #151515 55%, var(--bg-bottom) 100%);
    font-family: "Source Sans 3", "Myriad Pro", sans-serif;
  }
  .card {
    position: absolute;
    top: 306px;
    height: 270px;
    border-radius: 12px;
  }
  .card--front {
    left: 149px;
    width: 439px;
    background: var(--card-front);
  }
  .card--back {
    left: 608px;
    width: 441px;
    background: var(--card-back);
  }
  .wordmark {
    position: absolute;
    display: flex;
    align-items: center;
    justify-content: center;
    gap: 10px;
    color: var(--accent);
    font-weight: 600;
    line-height: 1;
  }
  .wordmark__dot {
    flex: none;
    border-radius: 50%;
    background: var(--accent);
  }
  .card--front .wordmark {
    left: 56px;
    top: 106px;
    width: 148px;
    height: 60px;
    font-size: 52px;
  }
  .card--front .wordmark__dot { width: 22px; height: 22px; }
  .card--back .wordmark {
    left: 0;
    right: 0;
    top: 88px;
    height: 50px;
    font-size: 44px;
  }
  .card--back .wordmark__dot { width: 18px; height: 18px; }
  .contact {
    position: absolute;
    left: 227px;
    top: 60px;
    color: var(--ink);
    font-size: 12.5px;
    line-height: 16px;
  }
  .contact__name {
    margin: 0;
    color: var(--accent);
    font-size: 15px;
    font-weight: 600;
    line-height: 18px;
  }
  .contact__role { margin: 0 0 10px; }
  .contact__address { margin: 0 0 11px; font-style: normal; }
  .contact__list { list-style: none; margin: 0; padding: 0; }
  .contact__item {
    display: flex;
    align-items: center;
    gap: 7px;
  }
  .contact__icon { width: 9px; height: 9px; flex: none; }
  .brand {
    position: absolute;
    left: 0;
    right: 0;
    top: 166px;
    text-align: center;
  }
  .brand__name {
    margin: 0;
    color: var(--accent);
    font-weight: 600;
    font-size: 30px;
    line-height: 34px;
    letter-spacing: 1px;
    text-transform: uppercase;
  }
  .brand__tagline {
    margin: 2px 0 0;
    color: var(--ink-dark);
    font-weight: 400;
    font-size: 14px;
    letter-spacing: 3px;
    line-height: 16px;
  }
</style>
</head>
<body>
<main class="stage">
  <section class="card card--front" aria-label="Card front">
    <div class="wordmark"><span class="wordmark__dot"></span><span>KR</span></div>
    <div class="contact">
      <h2 class="contact__name">Kara Reid</h2>
      <p class="contact__role">Managing Director</p>
      <address class="contact__address">12345, Address Goes Here<br>Country Name, 123456.</address>
      <ul class="contact__list">
        <li class="contact__item">
          <svg class="contact__icon" viewBox="0 0 10 10" aria-hidden="true"><path fill="var(--accent)" d="M2 0.5 L3.8 2.8 L2.8 4 Q4 6.2 6 7.2 L7.2 6.2 L9.5 8 L8.3 9.5 Q3.5 9 0.5 1.7 Z"/></svg>
          <span>044-987 654 321</span>
        </li>
        <li class="contact__item">
          <svg class="contact__icon" viewBox="0 0 10 10" aria-hidden="true"><rect x="0.5" y="2" width="9" height="6.5" fill="var(--accent)"/><path d="M0.8 2.4 L5 5.8 L9.2 2.4" stroke="#fff" stroke-width="1" fill="none"/></svg>
          <span>info@webname.com</span>
        </li>
        <li class="contact__item">
          <svg class="contact__icon" viewBox="0 0 10 10" aria-hidden="true"><circle cx="5" cy="5" r="4.5" fill="var(--accent)"/><path d="M2.5 3 Q4 4 3.5 6 M6 2 Q7.5 4 6.5 8" stroke="#fff" stroke-width="0.9" fill="none"/></svg>
          <span>www.websitename.com</span>
        </li>
      </ul>
    </div>
  </section>

  <section class="card card--back" aria-label="Card back">
    <div class="wordmark"><span class="wordmark__dot"></span><span>KR</span></div>
    <div class="brand">
      <h1 class="brand__name">Kara Reid</h1>
      <p class="brand__tagline">ORIGINAL FINE ARTWORKS</p>
    </div>
  </section>
</main>
</body>
</html>
```